Brindle Cyto company values interaction - arch and foundation

We need a graphic that represents the relationship between our company's values. Our company, Brindle Cyto, is a biotechnology startup based in Seattle. We are pushing the boundaries of biology to create tailored cell therapy solutions through protein design and custom programming to cure diseases. Our values are Respect, Inclusion, Science, Innovation and Collaboration. We view Respect and Inclusion as the foundation on which our other values rest, with Science and Collaboration supporting Innovation. We have styled this as an arch with Innovation in the middle (see attached file). We would like to show this graphic on our careers page to help candidates know what we're all about. See: https://www.brindlecyto.example/careers

Target Market(s)

Potential job applicants, current employees and anyone who wants to know what we're about

Industry/Entity Type

Biotechnology

Font styles to use
Sans Serif

Colors

Designer to choose colors to be used in the design.

Requirements
Must have
• A foundation that supports an arch to demonstrate how our values drive our culture and mission

```html
<!DOCTYPE html>
<html lang="en">
<head>
<meta charset="utf-8">
<title>Brindle Cyto – Our Values</title>
<link rel="stylesheet" href="https://fonts.googleapis.com/css2?family=Source+Sans+3:wght@700;800;900&display=swap">
<style>
  :root {
    --deep-blue: #0e67a8;
    --deep-blue-edge: #0a4f86;
    --aqua: #64cfd8;
    --aqua-edge: #3fb0ba;
    --paper: #ffffff;
    --label: #ffffff;
  }
  html, body {
    margin: 0;
    padding: 0;
    width: 1200px;
    height: 952px;
    overflow: hidden;
    background: var(--paper);
  }
  .values-arch {
    display: block;
    width: 1200px;
    height: 952px;
  }
  .value-label {
    font-family: "Source Sans 3", sans-serif;
    font-weight: 800;
    fill: var(--label);
    filter: url(#label-shadow);
  }
  .arch-label {
    font-size: 27px;
    font-variant: small-caps;
    letter-spacing: 0.5px;
  }
  .pillar-label {
    font-size: 82px;
    font-weight: 900;
  }
  .pillar-label.small-caps {
    font-variant: small-caps;
  }
  .stone-blue { fill: var(--deep-blue); stroke: var(--deep-blue-edge); stroke-width: 1.5; }
  .stone-aqua { fill: var(--aqua); stroke: var(--aqua-edge); stroke-width: 1.5; }
  .joint { stroke: var(--paper); stroke-width: 12; }
</style>
</head>
<body>
<svg class="values-arch" viewBox="0 0 1200 952" xmlns="http://www.w3.org/2000/svg" role="img" aria-label="Brindle Cyto values: Respect and Inclusion as pillars supporting an arch of Science, Innovation and Collaboration">
  <defs>
    <filter id="label-shadow" x="-10%" y="-10%" width="120%" height="130%">
      <feDropShadow dx="1.5" dy="2" stdDeviation="1.2" flood-color="#083a60" flood-opacity="0.55"/>
    </filter>
    <clipPath id="above-springline">
      <rect x="0" y="0" width="1200" height="390"/>
    </clipPath>
    <path id="arch-text-line" d="M 334 494 A 260 260 0 0 1 854 494"/>
  </defs>

  <!-- Arch voussoirs: centre (594,494), outer r 323, inner r 215 -->
  <g class="arch" clip-path="url(#above-springline)">
    <!-- Science: -80deg to -21deg -->
    <path class="stone-aqua" d="M 275.9 437.9 A 323 323 0 0 1 478.2 192.5 L 517 293.3 A 215 215 0 0 0 382.3 456.7 Z"/>
    <!-- Innovation: -21deg to 21deg -->
    <path class="stone-blue" d="M 478.2 192.5 A 323 323 0 0 1 709.8 192.5 L 671 293.3 A 215 215 0 0 0 517 293.3 Z"/>
    <!-- Collaboration: 21deg to 80deg -->
    <path class="stone-aqua" d="M 709.8 192.5 A 323 323 0 0 1 912.1 437.9 L 805.7 456.7 A 215 215 0 0 0 671 293.3 Z"/>
    <line class="joint" x1="478.2" y1="192.5" x2="517" y2="293.3"/>
    <line class="joint" x1="709.8" y1="192.5" x2="671" y2="293.3"/>
  </g>

  <text class="value-label arch-label">
    <textPath href="#arch-text-line" startOffset="24%" text-anchor="middle">Science</textPath>
  </text>
  <text class="value-label arch-label">
    <textPath href="#arch-text-line" startOffset="50%" text-anchor="middle">Innovation</textPath>
  </text>
  <text class="value-label arch-label">
    <textPath href="#arch-text-line" startOffset="75%" text-anchor="middle">Collaboration</textPath>
  </text>

  <!-- Foundation pillars -->
  <g class="pillar pillar-respect">
    <rect class="stone-blue" x="287" y="404" width="117" height="377"/>
    <text class="value-label pillar-label" transform="translate(372 716) rotate(-90)" textLength="262" lengthAdjust="spacingAndGlyphs">RESPECT</text>
  </g>
  <g class="pillar pillar-inclusion">
    <rect class="stone-blue" x="784" y="404" width="118" height="377"/>
    <text class="value-label pillar-label small-caps" transform="translate(868 747) rotate(-90)" textLength="322" lengthAdjust="spacingAndGlyphs">Inclusion</text>
  </g>
</svg>
</body>
</html>
```